VELNUKA Promotions - Business Card Design Project

We are looking for a classy business cards for Promotion Company based in Toronto, Canada named Velnuka Promotions.

Velnuka Promotions has an idea and vision to set high standard, be EXCLUSIVE and attract a group of people that will follow us through events we promote (night clubs, brand promotions, music events, and sport events)

We want to present a high standards and classy image to the others...
Updates

Target Market(s)

male/female age 25-40 Target: business owners young entrepreneur - clubing industry - media industry - promotion industry - marketing media industry

Industry/Entity Type

Events

Requirements
Must have
• business cards should be classy, make people feel exclusive , make people react ..

```html
<!DOCTYPE html>
<html lang="en">
<head>
<meta charset="utf-8">
<title>Velnuka Promotions – Business Card</title>
<link rel="stylesheet" href="https://fonts.googleapis.com/css2?family=Tinos:wght@400;700&family=Arimo&display=swap">
<style>
  :root {
    --backdrop: #e3e8e5;
    --card-black: #000000;
    --card-edge: #3a3f47;
    --accent-cyan: #2bb7d8;
    --text-white: #f2f2f2;
    --label-grey: #d6d6d6;
    --strip-blue-light: #5d84d6;
    --strip-blue-dark: #0b1020;
  }
  * { margin: 0; padding: 0; box-sizing: border-box; }
  html, body { width: 1200px; height: 759px; overflow: hidden; }
  body {
    background: var(--backdrop);
    font-family: "Tinos", "Times New Roman", serif;
    position: relative;
  }
  .card {
    position: absolute;
    top: 238px;
    width: 490px;
    height: 282px;
    background: var(--card-black);
    box-shadow: 0 6px 18px rgba(0,0,0,0.25);
  }
  .card--front { left: 75px; }
  .card--back {
    left: 635px;
    border: 3px solid var(--card-edge);
  }

  .brand-name {
    position: absolute;
    left: 210px;
    top: 124px;
    color: var(--accent-cyan);
    font-size: 27px;
    font-weight: 400;
    letter-spacing: 1px;
    white-space: nowrap;
  }

  .accent-strip {
    position: absolute;
    left: 3px;
    top: 3px;
    bottom: 3px;
    width: 100px;
    background: linear-gradient(90deg, var(--strip-blue-light) 0%, #3551a0 45%, var(--strip-blue-dark) 100%);
  }

  .holder-name {
    position: absolute;
    right: 36px;
    top: 138px;
    color: var(--accent-cyan);
    font-size: 27px;
    font-weight: 400;
    white-space: nowrap;
  }
  .holder-title {
    position: absolute;
    left: 255px;
    top: 169px;
    color: var(--text-white);
    font-size: 16px;
    font-weight: 700;
    white-space: nowrap;
  }

  .contact-list {
    position: absolute;
    left: 110px;
    top: 198px;
    list-style: none;
  }
  .contact-item {
    display: flex;
    align-items: center;
    height: 22px;
  }
  .contact-label {
    width: 54px;
    text-align: right;
    color: var(--label-grey);
    font-family: "Arimo", Arial, sans-serif;
    font-size: 14px;
    display: flex;
    justify-content: flex-end;
    align-items: center;
    gap: 1px;
  }
  .contact-value {
    margin-left: 18px;
    color: var(--accent-cyan);
    font-size: 15px;
    white-space: nowrap;
  }
  .globe-icon { width: 15px; height: 15px; }
</style>
</head>
<body>
  <section class="card card--front" aria-label="Card front">
    <span class="brand-name">VELNUKA Promotions</span>
  </section>

  <section class="card card--back" aria-label="Card back">
    <div class="accent-strip"></div>
    <h1 class="holder-name">Marcus Delaney's</h1>
    <p class="holder-title">Promotion Director</p>
    <ul class="contact-list">
      <li class="contact-item">
        <span class="contact-label">@:</span>
        <span class="contact-value">marcusdelaney@velnukapromo.com</span>
      </li>
      <li class="contact-item">
        <span class="contact-label">Mob:</span>
        <span class="contact-value">07700900481</span>
      </li>
      <li class="contact-item">
        <span class="contact-label">
          <svg class="globe-icon" viewBox="0 0 16 16" aria-hidden="true">
            <g fill="none" stroke="#cfcfcf" stroke-width="1.2">
              <circle cx="8" cy="8" r="6.6"/>
              <ellipse cx="8" cy="8" rx="3" ry="6.6"/>
              <line x1="1.4" y1="8" x2="14.6" y2="8"/>
              <line x1="2.5" y1="4.6" x2="13.5" y2="4.6"/>
              <line x1="2.5" y1="11.4" x2="13.5" y2="11.4"/>
            </g>
          </svg>:
        </span>
        <span class="contact-value">velnukapromo.com</span>
      </li>
    </ul>
  </section>
</body>
</html>
```